Skin Care Branding / Package design

We are a manufacturer of consumable hemp products and have some skin care products we want to group into a brand of its own, under our primary brand which is TulaMoss.  our website is www.tulamossgoods.example
Our current packaging was developed on the fly with little or no thought given to a sub brand concept.  We have sub branded other products such as Quiet Fern, Willow Crest, and Harbin.  While TulaMoss appears on the packaging it is not the predominate brand.
The products will be sold in cosmetic stores, health stores, medspas, pharmacies and other upscale stores.  We want the appeal to be elegant & upscale and stand out on the shelf.
We are open to changing the jar, bottle or container and look forward to any recommendations on this.
Later we will need flyers, social media ads, and other graphics.
Our primary goal is to create designs for each of our products that are consistent and create another sub brand.
We are also open to changing the names of these products.
images of the existing products are attached, we plan to add more skin care products.

```html
<!DOCTYPE html>
<html lang="en">
<head>
<meta charset="utf-8">
<title>TulaMoss Skin Care Labels</title>
<link href="https://fonts.googleapis.com/css2?family=Archivo:wght@400;700;800&family=Roboto:wght@400;500&display=swap" rel="stylesheet">
<style>
  :root {
    --backdrop: #e8e8e8;
    --white: #ffffff;
    --lavender: #7e2b8c;
    --lavender-dark: #6a2478;
    --coral: #e8727a;
    --coral-ink: #e25b63;
    --periwinkle: #9a95f0;
    --periwinkle-ink: #8a85e6;
    --citrus: #f0c93a;
    --citrus-ink: #d9a916;
    --sage: #a3cf7e;
    --sage-ink: #7fb457;
  }
  * { box-sizing: border-box; margin: 0; padding: 0; }
  html, body { width: 1200px; height: 800px; overflow: hidden; }
  body {
    background: var(--backdrop);
    position: relative;
    font-family: "Roboto", Arial, sans-serif;
    color: var(--white);
  }
  .label {
    position: absolute;
    display: flex;
    flex-direction: column;
    box-shadow: 0 6px 18px rgba(0,0,0,0.08);
  }
  .label-face {
    position: relative;
    flex: 1;
    display: flex;
    flex-direction: column;
    align-items: center;
    text-align: center;
  }
  .label-foot {
    height: 30px;
    flex: 0 0 auto;
    background: var(--white);
    display: flex;
    align-items: center;
    justify-content: center;
    font-size: 7px;
    letter-spacing: 0.2px;
  }
  .brand-name {
    font-family: "Archivo", Arial, sans-serif;
    font-weight: 800;
    font-size: 15px;
    letter-spacing: 1px;
    color: var(--white);
    text-transform: uppercase;
    white-space: nowrap;
  }
  .product-name {
    font-family: "Archivo", Arial, sans-serif;
    font-weight: 700;
    line-height: 1.05;
    white-space: nowrap;
  }
  .product-sub { font-weight: 400; line-height: 1.1; white-space: nowrap; }
  .dose-title {
    font-size: 7px;
    letter-spacing: 1px;
    text-transform: uppercase;
    padding: 0 6px 2px;
    border-bottom: 0.5px solid rgba(255,255,255,0.7);
  }
  .dose-line { font-size: 8px; margin-top: 3px; white-space: nowrap; }
  .dose-line .divider { display: inline-block; width: 0.5px; height: 9px; background: rgba(255,255,255,0.8); margin: 0 4px; vertical-align: middle; }
  .side-note {
    position: absolute;
    left: 6px;
    bottom: 16px;
    writing-mode: vertical-rl;
    transform: rotate(180deg);
    font-size: 5.5px;
    letter-spacing: 1.2px;
    text-transform: uppercase;
    opacity: 0.7;
    white-space: nowrap;
  }

  /* Calming lotion */
  .label-lotion { left: 56px; top: 360px; width: 152px; height: 262px; }
  .label-lotion .label-face { background: var(--lavender); padding-top: 40px; }
  .label-lotion .brand-name { margin-bottom: 56px; }
  .label-lotion .product-name { font-size: 18px; }
  .label-lotion .product-sub { font-size: 11px; margin-bottom: 38px; }
  .label-lotion .label-foot { color: var(--lavender-dark); }

  /* Facial serum */
  .label-serum { left: 244px; top: 420px; width: 140px; height: 210px; }
  .label-serum .label-face { background: var(--coral); padding-top: 32px; }
  .label-serum .brand-name { margin-bottom: 42px; }
  .label-serum .product-name { font-size: 14px; }
  .label-serum .product-sub { font-size: 9px; margin-bottom: 32px; }
  .label-serum .label-foot { color: var(--coral-ink); }

  /* Move roll-on */
  .label-rollon { left: 412px; top: 410px; width: 140px; height: 222px; }
  .label-rollon .label-face { background: var(--periwinkle); padding-top: 34px; }
  .label-rollon .brand-name { margin-bottom: 46px; }
  .label-rollon .product-name { font-size: 15px; }
  .label-rollon .product-sub { font-size: 9.5px; margin-bottom: 34px; }
  .label-rollon .label-foot { color: var(--periwinkle-ink); }

  /* Wide jar labels */
  .label-wide .label-face {
    flex-direction: row;
    align-items: stretch;
    text-align: left;
    padding: 14px 14px 8px 22px;
  }
  .label-wide .brand-col { flex: 0 0 auto; padding-top: 16px; margin-right: 14px; }
  .label-wide .brand-name { font-size: 13px; }
  .label-wide .info-col { flex: 1; min-width: 0; display: flex; flex-direction: column; }
  .label-wide .dose { margin-top: auto; align-self: flex-end; text-align: center; }
  .label-wide .side-note { bottom: 8px; left: 5px; }
  .label-wide .label-foot { height: 24px; }

  .label-vitamin { left: 584px; top: 532px; width: 262px; height: 118px; }
  .label-vitamin .label-face { background: var(--citrus); }
  .label-vitamin .product-name { font-size: 21px; }
  .label-vitamin .product-sub { font-size: 18px; }
  .label-vitamin .label-foot { color: var(--citrus-ink); font-size: 8px; }

  .label-muscle { left: 862px; top: 550px; width: 278px; height: 104px; }
  .label-muscle .label-face { background: var(--sage); }
  .label-muscle .product-name { font-size: 16px; }
  .label-muscle .product-sub { font-size: 12px; }
  .label-muscle .label-foot { color: var(--sage-ink); }
</style>
</head>
<body>

  <section class="label label-lotion">
    <div class="label-face">
      <span class="side-note">Infused Daily Moisturizer</span>
      <div class="brand-name">TulaMoss</div>
      <h2 class="product-name">Calming</h2>
      <p class="product-sub">Lavander Lotion</p>
      <p class="dose-title">CBD + CBG</p>
      <p class="dose-line">50/50 Blend<span class="divider"></span>800mg</p>
    </div>
    <div class="label-foot">4FL OZ / 120ML</div>
  </section>

  <section class="label label-serum">
    <div class="label-face">
      <span class="side-note">Tone | Hydrate | Soften</span>
      <div class="brand-name">TulaMoss</div>
      <h2 class="product-name">Facial Serum</h2>
      <p class="product-sub">For Beauty</p>
      <p class="dose-title">CBG Infused</p>
      <p class="dose-line">300mg CBG</p>
    </div>
    <div class="label-foot">NET WT .5 OZ / 15G</div>
  </section>

  <section class="label label-rollon">
    <div class="label-face">
      <div class="brand-name">TulaMoss</div>
      <h2 class="product-name">Move</h2>
      <p class="product-sub">Gel Muscle Roll-On</p>
      <p class="dose-title">Cannabiniods</p>
      <p class="dose-line">50/50 Blend Of<span class="divider"></span>6000mg</p>
    </div>
    <div class="label-foot">NET WT 3 OZ / 90G</div>
  </section>

  <section class="label label-wide label-vitamin">
    <div class="label-face">
      <span class="side-note">Brighten + Hydrate</span>
      <div class="brand-col"><div class="brand-name">TulaMoss</div></div>
      <div class="info-col">
        <h2 class="product-name">Vitamin C</h2>
        <p class="product-sub">Cream</p>
        <div class="dose">
          <p class="dose-title">CBG Infused</p>
          <p class="dose-line">For Beauty<span class="divider"></span>300mg CBG</p>
        </div>
      </div>
    </div>
    <div class="label-foot">NET WT .5 OZ / 15G</div>
  </section>

  <section class="label label-wide label-muscle">
    <div class="label-face">
      <div class="brand-col"><div class="brand-name">TulaMoss</div></div>
      <div class="info-col">
        <h2 class="product-name">Muscle &amp; Joint</h2>
        <p class="product-sub">Cream</p>
        <div class="dose">
          <p class="dose-title">CBD + CBG</p>
          <p class="dose-line">Full Spectrum<span class="divider"></span>1500mg</p>
        </div>
      </div>
    </div>
    <div class="label-foot">NET WT 1 OZ / 30G</div>
  </section>

</body>
</html>
```